Pale Lanterns Old Lane Walk Poster Design

We need an A4 sized poster to promote our weekly true crime tours. This poster will be posted onto community noticeboards.
Lots of information and images can be viewed at the following links:-
www.palelanterns.com.au
www.palelanterns.com.au/bookings/
https://www.facebook.com/palelanternsoldlane/
https://www.examplereviews.com.au/Attraction_Review-g000000-d00000000-Reviews-Pale_Lanterns-Newcastle_Greater_Newcastle_New_South_Wales.html
There are also a number of images for possible use at the following link - we are open to intepretation:-
http://palelanterns.com.au/tour-photographs/
The font on our website is "SpecialElite" so we would like to continue using that font type.
Target Market(s)
Adults 25-65.
Font styles to use
Other font styles liked:
- Special Elite
Colors
Designer to choose colors to be used in the design.
Look and feel
Each slider illustrates characteristics of the customer's brand and the style your logo design should communicate.

```html
<!DOCTYPE html>
<html lang="en">
<head>
<meta charset="utf-8">
<title>Pale Lanterns Old Lane Walk Poster</title>
<link rel="stylesheet" href="https://fonts.googleapis.com/css2?family=Special+Elite&family=Roboto+Condensed:wght@400;700&family=Archivo+Black&display=swap">
<style>
  :root {
    --backdrop: #3a2a20;
    --paper-light: #f3e6c0;
    --paper-mid: #e9d6a0;
    --paper-edge: #d6b874;
    --ink: #1c1c1c;
    --body-ink: #2f2f2f;
    --accent-red: #d9232d;
    --tag-grey: #6d6e71;
    --tag-text: #f1f1f1;
    --band-grey: #6a6b6e;
    --band-dark: #55565a;
    --photo-light: #b9b9b9;
    --photo-dark: #2e2e2e;
  }
  * { margin: 0; padding: 0; box-sizing: border-box; }
  html, body {
    width: 1200px; height: 1200px; overflow: hidden;
    background: var(--backdrop);
  }
  .poster {
    position: absolute; left: 204px; top: 40px;
    width: 792px; height: 1120px; overflow: hidden;
    background:
      radial-gradient(ellipse at 45% 40%, var(--paper-light) 0%, var(--paper-mid) 60%, var(--paper-edge) 100%);
    box-shadow: 0 6px 18px rgba(0,0,0,0.45);
  }
  .brand-name {
    position: absolute; left: 24px; top: 160px;
    font-family: "Special Elite", monospace;
    font-size: 46px; color: var(--ink); letter-spacing: 1px;
  }
  .tour-title {
    position: absolute; left: 30px; top: 262px;
    font-family: "Special Elite", monospace;
    font-size: 66px; line-height: 64px; color: var(--ink);
  }
  .tour-photo {
    position: absolute; left: 242px; top: 189px;
    width: 652px; height: 652px; border-radius: 50%;
    border: 4px solid #fff;
    background: radial-gradient(circle at 55% 30%, var(--photo-light) 0%, #7a7a7a 45%, var(--photo-dark) 100%);
    box-shadow: -8px 4px 20px rgba(0,0,0,0.35);
  }
  .tour-facts {
    position: absolute; left: 394px; top: 600px;
    color: #fff; text-shadow: 1px 2px 3px rgba(0,0,0,0.7);
  }
  .tour-price {
    font-family: "Archivo Black", sans-serif;
    font-size: 58px; line-height: 66px;
  }
  .tour-detail {
    font-family: "Roboto Condensed", sans-serif;
    font-size: 31px; line-height: 42px;
  }
  .claim-tag {
    position: absolute; left: 0; height: 52px;
    background: var(--tag-grey); color: var(--tag-text);
    font-family: "Special Elite", monospace; font-size: 32px;
    line-height: 52px; padding-left: 22px;
    border-radius: 0 26px 26px 0;
  }
  .claim-true { top: 693px; width: 242px; }
  .claim-unbelievable { top: 772px; width: 380px; }
  .tour-pitch {
    position: absolute; left: 92px; top: 860px; width: 680px;
  }
  .pitch-heading {
    font-family: "Roboto Condensed", sans-serif; font-weight: 700;
    font-size: 21px; color: var(--accent-red); margin-bottom: 8px;
  }
  .pitch-list {
    list-style: none;
    font-family: "Roboto Condensed", sans-serif;
    font-size: 17px; line-height: 29px; color: var(--body-ink);
  }
  .pitch-list li::before {
    content: "\2022"; display: inline-block; width: 18px;
  }
  .booking-band {
    position: absolute; left: 0; bottom: 0; width: 100%; height: 63px;
    border-top: 2px solid var(--accent-red);
    background: linear-gradient(var(--band-grey), var(--band-dark));
    font-family: "Special Elite", monospace; font-size: 27px;
    color: #2b2b2b; line-height: 46px; padding-left: 24px;
  }
</style>
</head>
<body>
  <div class="poster">
    <div class="brand-name">PALE LANTERNS</div>
    <h1 class="tour-title">True<br>Crime<br>Tour</h1>

    <div class="tour-photo" role="img" aria-label="Black and white photograph of an old tram in heavy rain on a city street"></div>

    <div class="tour-facts">
      <div class="tour-price">$34.00</div>
      <div class="tour-detail">Duration: 90 Minutes (approx.)</div>
      <div class="tour-detail">Location: Newcastle East, NSW</div>
    </div>

    <div class="claim-tag claim-true">100% TRUE</div>
    <div class="claim-tag claim-unbelievable">100% UNBELIEVABLE</div>

    <div class="tour-pitch">
      <h2 class="pitch-heading">TAKE A WALK ON THE DARK SIDE - REVISIT THE SCENES OF THE CRIMES.</h2>
      <ul class="pitch-list">
        <li>Retrace the steps of Newcastle's most infamous murderers.</li>
        <li>Descend into the murky world of fraudsters, adulterers and lordly impersonators.</li>
        <li>Unearth the keys to the heart of the Tomahawk Murderer.</li>
        <li>Relive a time that proves truth is far stranger than fiction.</li>
        <li>Book your ticket for a unique investigation into a dark and crime ridden history.</li>
      </ul>
    </div>

    <div class="booking-band">for booking : www.palelanterns.com.au/bookings</div>
  </div>
</body>
</html>
```